Wix web design for healthcare IT consulting firm.

I am looking for a web design built in Wix that it will be easy for me to add or edit content in the future. The web site does not need to be overly complicated, but it should look very polished and professional. I also want to ensure it is mobile device friendly. I do not need any type of on-line purchasing ability. I will eventually do blogs, but for now it is a fairly standard web site with main page, about us, services provided, etc. I would also like a place for potential customers to contact us directly from the web site. I have included a Word document with some content for the web design. I have also included my logo and business card for reference. I would like to utilize similar colors as my business card. One of my primary competitors is https://vontalmhc.example/

Target Market(s)

Target market could be nursing home CEO, CIO, or other leader at an organization that manages long term care facilities.

Number of Pages Required

5+ page

Colors
876aae

Requirements
Must have
• Be designed to be used in Wix. Use the content I provided to create and make web design. Allow to be viewed on mobile device. Please use similar color structure as attached business card. Please use attached logo in design.

```html
<!DOCTYPE html>
<html lang="en">
<head>
<meta charset="utf-8">
<title>Brightway Healthcare Solutions</title>
<link href="https://fonts.googleapis.com/css2?family=Montserrat:wght@400;600;700&family=Roboto:wght@300;400;500&display=swap" rel="stylesheet">
<style>
:root{
  --purple:#6a4a9e;
  --purple-card:#7654a8;
  --purple-soft:rgba(160,110,230,.78);
  --ink:#222226;
  --body:#3a3a3e;
  --footer:#2b2a2e;
  --white:#ffffff;
}
*{box-sizing:border-box;margin:0;padding:0}
html,body{width:1200px;height:3056px;overflow:hidden;background:var(--white)}
body{position:relative;font-family:'Roboto',sans-serif;color:var(--body)}
.abs{position:absolute}
/* header */
.header{top:0;left:0;width:1200px;height:77px;background:var(--white)}
.brand{left:0;top:0;width:182px;height:77px;background:var(--purple);display:flex;align-items:center;justify-content:center;color:var(--white);font-family:'Montserrat',sans-serif;font-weight:700;font-size:21px}
.nav{left:430px;top:30px;display:flex;gap:36px;font-family:'Montserrat',sans-serif;font-weight:600;font-size:13px;color:var(--ink)}
.nav .active{color:var(--purple)}
.social-bar{left:873px;top:0;width:327px;height:77px;background:var(--purple);display:flex;align-items:center;justify-content:center;gap:26px}
.dot{width:18px;height:18px;border-radius:50%;background:var(--white)}
/* hero */
.hero{top:77px;left:0;width:1200px;height:520px;background:linear-gradient(120deg,#cfd3dc 0%,#eef0f4 40%,#f6f4f2 70%,#f1c9a8 100%)}
.hero-kicker{top:215px;width:1200px;text-align:center;font-family:'Roboto',sans-serif;font-weight:300;font-size:29px;color:var(--ink)}
.hero-title{top:268px;width:1200px;text-align:center;font-family:'Montserrat',sans-serif;font-weight:700;font-size:38px;line-height:53px;color:var(--purple)}
.btn{background:var(--purple);color:var(--white);font-family:'Montserrat',sans-serif;font-weight:600;text-transform:uppercase;display:flex;align-items:center;justify-content:center}
.hero-btn{left:506px;top:405px;width:189px;height:47px;font-size:15px}
/* split sections */
.photo{background:linear-gradient(135deg,#9aa7b5,#dfe5ea 50%,#7d8a99)}
.frame{border:2px solid var(--purple)}
h2.section{font-family:'Montserrat',sans-serif;font-weight:700;font-size:38px;color:var(--ink)}
.para{font-size:14px;line-height:34px;color:var(--body)}
.sub{font-family:'Montserrat',sans-serif;font-weight:600;font-size:17px;color:var(--purple)}
.ticks{list-style:none}
.ticks li{display:flex;align-items:center;gap:18px;font-size:14px;height:34px;color:var(--ink)}
.ticks svg{flex:none}
/* blog */
.blog{top:1730px;left:0;width:1200px;height:478px;background:linear-gradient(100deg,#b9c4cc,#dbe5ea 50%,#a9c6d3)}
.blog-box{left:356px;top:1787px;width:489px;height:363px;background:var(--purple-soft);text-align:center;color:var(--white)}
.blog-box h2{margin-top:54px;font-family:'Montserrat',sans-serif;font-weight:700;font-size:36px}
.blog-box p{margin:24px auto 0;width:420px;font-size:14px;line-height:29px}
.blog-links{margin-top:22px;display:flex;justify-content:center;gap:44px;font-size:14px}
.blog-links span{text-decoration:underline}
.blog-btn{left:508px;top:2052px;width:185px;height:38px;font-size:14px;background:#5b3f8a}
/* services */
.services-title{top:2290px;width:1200px;text-align:center}
.card{top:2385px;width:284px;height:372px;background:var(--purple-card);color:var(--white);text-align:center;padding-top:38px}
.card h3{margin-top:22px;font-family:'Roboto',sans-serif;font-weight:400;font-size:21px;line-height:32px;text-decoration:underline}
.card p{margin:16px auto 0;width:230px;font-size:13px;line-height:24px}
.card .more{position:absolute;left:0;bottom:20px;width:100%;font-size:13px;font-weight:500;text-decoration:underline}
/* footer */
.footer{top:2846px;left:0;width:1200px;height:210px;background:var(--footer);color:var(--white);font-size:13px}
.f-line{width:1200px;display:flex;justify-content:center;align-items:center;gap:16px}
.f-social{display:flex;justify-content:center;gap:26px}
.f-social .dot{width:15px;height:15px}
</style>
</head>
<body>
<header class="abs header">
  <div class="abs brand">Brightway</div>
  <nav class="abs nav"><span class="active">HOME</span><span>ABOUT US</span><span>SERVICES</span><span>CONTACT US</span></nav>
  <div class="abs social-bar"><span class="dot"></span><span class="dot"></span><span class="dot"></span><span class="dot"></span></div>
</header>

<section class="abs hero" role="img" aria-label="Hands using a tablet with floating healthcare icons"></section>
<div class="abs hero-kicker">Brightway Healthcare Solutions</div>
<h1 class="abs hero-title">Increasing the value and security of<br>your technology resources</h1>
<div class="abs btn hero-btn">Learn More</div>

<!-- about -->
<div class="abs frame" style="left:33px;top:714px;width:526px;height:405px"></div>
<div class="abs photo" style="left:59px;top:686px;width:526px;height:408px" role="img" aria-label="Doctors meeting around a laptop"></div>
<h2 class="abs section" style="left:654px;top:706px">ABOUT US</h2>
<p class="abs para" style="left:654px;top:772px;width:414px">Lorem ipsum dolor sit amet, consectetur adipiscing elit, sed do eiusmod tempor incididunt ut labore et dolore magna aliqua. Ut enim ad minim veniam, quis nostrud exercitation ullamco laboris nisi ut aliquip ex ea commodo consequat.</p>
<div class="abs sub" style="left:654px;top:928px">Brightway Niche</div>
<ul class="abs ticks" style="left:652px;top:968px">
  <li><svg width="14" height="14" viewBox="0 0 14 14"><circle cx="7" cy="7" r="7" fill="#6a4a9e"/><path d="M3.8 7.2l2.2 2.1 4.2-4.3" stroke="#fff" stroke-width="1.6" fill="none"/></svg>Understand and get to know customer and their needs</li>
  <li><svg width="14" height="14" viewBox="0 0 14 14"><circle cx="7" cy="7" r="7" fill="#6a4a9e"/><path d="M3.8 7.2l2.2 2.1 4.2-4.3" stroke="#fff" stroke-width="1.6" fill="none"/></svg>Committed to be a partner, not vendor</li>
  <li><svg width="14" height="14" viewBox="0 0 14 14"><circle cx="7" cy="7" r="7" fill="#6a4a9e"/><path d="M3.8 7.2l2.2 2.1 4.2-4.3" stroke="#fff" stroke-width="1.6" fill="none"/></svg>Provide simplified change management expertise</li>
</ul>

<!-- mission -->
<h2 class="abs section" style="left:128px;top:1244px">MISSION STATEMENT</h2>
<p class="abs para" style="left:128px;top:1308px">Partner with customers to increase the value of their technology tools</p>
<div class="abs sub" style="left:128px;top:1370px">Core Values</div>
<ul class="abs ticks" style="left:126px;top:1407px">
  <li><svg width="14" height="14" viewBox="0 0 14 14"><circle cx="7" cy="7" r="7" fill="#6a4a9e"/><path d="M3.8 7.2l2.2 2.1 4.2-4.3" stroke="#fff" stroke-width="1.6" fill="none"/></svg>Customer Focused</li>
  <li><svg width="14" height="14" viewBox="0 0 14 14"><circle cx="7" cy="7" r="7" fill="#6a4a9e"/><path d="M3.8 7.2l2.2 2.1 4.2-4.3" stroke="#fff" stroke-width="1.6" fill="none"/></svg>Integrity &amp; Ethics</li>
  <li><svg width="14" height="14" viewBox="0 0 14 14"><circle cx="7" cy="7" r="7" fill="#6a4a9e"/><path d="M3.8 7.2l2.2 2.1 4.2-4.3" stroke="#fff" stroke-width="1.6" fill="none"/></svg>Practice Accountability</li>
  <li><svg width="14" height="14" viewBox="0 0 14 14"><circle cx="7" cy="7" r="7" fill="#6a4a9e"/><path d="M3.8 7.2l2.2 2.1 4.2-4.3" stroke="#fff" stroke-width="1.6" fill="none"/></svg>Professional Development</li>
  <li><svg width="14" height="14" viewBox="0 0 14 14"><circle cx="7" cy="7" r="7" fill="#6a4a9e"/><path d="M3.8 7.2l2.2 2.1 4.2-4.3" stroke="#fff" stroke-width="1.6" fill="none"/></svg>Have Fun</li>
</ul>
<div class="abs frame" style="left:640px;top:1234px;width:526px;height:406px"></div>
<div class="abs photo" style="left:615px;top:1208px;width:526px;height:408px;background:linear-gradient(135deg,#e8ecef,#f6f4f1 50%,#c9d3db)" role="img" aria-label="Doctor reviewing a chart with an older patient"></div>

<!-- blog -->
<section class="abs blog" role="img" aria-label="Doctor with stethoscope and digital medical records display"></section>
<div class="abs blog-box">
  <h2>OUR LATEST BLOG</h2>
  <p>Lorem ipsum dolor sit amet, consectetur adipiscing elit, sed do eiusmod tempor incididunt ut labore et dolore</p>
  <div class="blog-links"><span>View</span><span>Learn More</span></div>
</div>
<div class="abs btn blog-btn">News &amp; Updates</div>

<!-- services -->
<h2 class="abs section services-title">OUR SERVICES</h2>
<article class="abs card" style="left:287px">
  <svg width="60" height="56" viewBox="0 0 60 56" fill="none" stroke="#fff" stroke-width="2.5"><rect x="4" y="4" width="52" height="36" rx="2"/><path d="M10 26l8-6 6 6 8-10 8 8 10-6"/><path d="M24 40v8M36 40v8M18 50h24"/></svg>
  <h3>Electronic Health<br>Record (EHR) Services</h3>
  <p>Provide guidance and resources to assist with improving the effective use of the customer's EHR system.</p>
  <span class="more">Learn More</span>
</article>
<article class="abs card" style="left:629px">
  <svg width="64" height="56" viewBox="0 0 64 56" fill="none" stroke="#fff" stroke-width="2.5"><path d="M16 38a11 11 0 0 1 2-22 15 15 0 0 1 28 2 10 10 0 0 1 2 20z"/><circle cx="32" cy="30" r="6"/><path d="M24 38v8M32 38v12M40 38v8"/><circle cx="24" cy="48" r="2"/><circle cx="40" cy="48" r="2"/></svg>
  <h3>Information<br>Technology Services</h3>
  <p>Provide comprehensive risk assessment including identifying all risks associated with the customer's electronic protected health information (ePHI).</p>
  <span class="more">Learn More</span>
</article>

<!-- footer -->
<footer class="abs footer">
  <div class="abs f-line" style="top:56px"><svg width="14" height="11" viewBox="0 0 14 11"><rect width="14" height="11" fill="#fff"/><path d="M0 0l7 6 7-6" stroke="#2b2a2e" stroke-width="1.4" fill="none"/></svg><span style="text-decoration:underline">Email us at contact@brightwayhcs.example</span></div>
  <div class="abs f-line" style="top:92px"><svg width="12" height="12" viewBox="0 0 24 24"><path fill="#fff" d="M6.6 10.8a15 15 0 0 0 6.6 6.6l2.2-2.2a1 1 0 0 1 1-.25 11.4 11.4 0 0 0 3.6.6 1 1 0 0 1 1 1V20a1 1 0 0 1-1 1A17 17 0 0 1 3 4a1 1 0 0 1 1-1h3.5a1 1 0 0 1 1 1c0 1.25.2 2.45.6 3.6a1 1 0 0 1-.25 1z"/></svg><span>Call us at 555-014-2290</span></div>
  <div class="abs f-social" style="top:140px;width:1200px"><span class="dot"></span><span class="dot"></span><span class="dot"></span><span class="dot"></span></div>
  <div class="abs f-line" style="top:174px;gap:14px"><span>© 2018 Copyrights Brightway. All Rights Reserved</span><span>|</span><span>Privacy Policy</span><span>|</span><span>Terms &amp; Services.</span></div>
</footer>
</body>
</html>
```